Post storm repair flyer

looking for an eye catching 6x9 postcard to send out to single family home owners advertising a "Post Storm Repair Special" explaining that after the recent hurricanes its very important to have your roof checked and any repairs fixed right away before they become a bigger more costly problem and that even though your home wasn't directly hit by the storm the high wind gust could've cause unseen damage.
offer $200 off any repair *some rules may apply
Lark Roofing
888.417.LARK
www.LarkRoofing.example

Roofing

```html
<!DOCTYPE html>
<html lang="en">
<head>
<meta charset="utf-8">
<title>Lark Roofing – Post Storm Repair Special Postcard</title>
<link rel="stylesheet" href="https://fonts.googleapis.com/css2?family=Montserrat:wght@300;400;500;600;800&family=Rubik:ital,wght@0,500;0,700;1,400&display=swap">
<style>
  :root {
    --backdrop: #ecebe8;
    --honey: #e9b23a;
    --amber: #c28a12;
    --badge: #ffcc00;
    --charcoal: #3d3d3d;
    --ink: #1a1a1a;
    --offer-red: #e3101b;
    --paper: #ffffff;
    --rule: #b9b9b9;
  }
  html, body {
    margin: 0;
    width: 1200px;
    height: 1086px;
    overflow: hidden;
    background: var(--backdrop);
  }
  .postcard {
    position: absolute;
    left: 253px;
    width: 694px;
    height: 469px;
    display: block;
    box-shadow: 0 6px 18px rgba(0,0,0,.25);
  }
  .postcard--front { top: 54px; }
  .postcard--back { top: 554px; }
  .headline, .subhead, .body-copy, .brand-name, .phone-number {
    font-family: "Montserrat", sans-serif;
  }
  .badge-text { font-family: "Rubik", sans-serif; }
</style>
</head>
<body>

<svg class="postcard postcard--front" viewBox="0 0 867 586" aria-label="Postcard front">
  <defs>
    <linearGradient id="frontPhotoTone" x1="0" y1="0" x2="0" y2="1">
      <stop offset="0" stop-color="#7f8a96"/>
      <stop offset="0.45" stop-color="#5b5f66"/>
      <stop offset="0.75" stop-color="#d9d9d6"/>
      <stop offset="1" stop-color="#8b8f7e"/>
    </linearGradient>
  </defs>
  <rect class="photo" width="867" height="586" fill="url(#frontPhotoTone)" role="img" aria-label="Photo of roofers replacing shingles on a large white two-storey house"/>
  <polygon class="slate-panel" points="428,358 867,246 867,505" fill="var(--charcoal)"/>
  <polygon class="slate-edge" points="428,358 867,246 867,252 440,356" fill="#e6e6e6"/>
  <polygon class="amber-stripe" points="0,204 867,496 867,516 0,222" fill="var(--amber)"/>
  <polygon class="honey-field" points="0,220 867,513 867,586 0,586" fill="var(--honey)"/>

  <g class="brand">
    <circle cx="96" cy="306" r="26" fill="none" stroke="var(--paper)" stroke-width="4"/>
    <text class="brand-name" x="35" y="362" font-size="12" font-weight="500" fill="var(--paper)">LARKROOFING.EXAMPLE</text>
  </g>

  <text class="headline" x="28" y="425" font-size="54" fill="var(--ink)" letter-spacing="-1"><tspan font-weight="400">POST </tspan><tspan font-weight="800">STORM</tspan></text>
  <text class="headline" x="30" y="471" font-size="44" fill="var(--paper)" letter-spacing="-1"><tspan font-weight="800">REPAIR </tspan><tspan font-weight="400">SPECIAL</tspan></text>

  <text class="body-copy" font-size="17" fill="var(--ink)">
    <tspan x="31" y="510">After the recent hurricanes, it’s crucial to</tspan>
    <tspan x="31" y="531">have your roof inspected and any</tspan>
    <tspan x="31" y="552">necessary repairs made promptly.</tspan>
  </text>

  <g class="offer-badge" transform="translate(694 364)">
    <polygon points="0,-97 87,-48 87,48 0,97 -87,48 -87,-48" fill="var(--badge)" stroke="var(--amber)" stroke-width="4"/>
    <polyline points="-56,-20 0,-52 56,-20" fill="none" stroke="var(--ink)" stroke-width="12" stroke-linejoin="miter"/>
    <text class="badge-text" x="0" y="-8" text-anchor="middle" font-size="20" font-weight="700" fill="var(--ink)">Get</text>
    <text class="badge-text" x="0" y="22" text-anchor="middle" font-size="31" font-weight="700" fill="var(--offer-red)">$200 off</text>
    <text class="badge-text" x="0" y="44" text-anchor="middle" font-size="20" font-weight="500" fill="var(--ink)">any repair</text>
    <text class="badge-text" x="0" y="60" text-anchor="middle" font-size="11" font-style="italic" fill="var(--ink)">*some rules</text>
    <text class="badge-text" x="0" y="70" text-anchor="middle" font-size="11" font-style="italic" fill="var(--ink)">may apply</text>
  </g>

  <g class="phone" fill="none" stroke="var(--paper)" stroke-width="2.5">
    <circle cx="534" cy="523" r="16"/>
    <path d="M527 514 l5 -1 l3 6 l-3 2 q2 5 7 8 l2 -3 l6 3 l-1 5 q-12 1 -19 -20 z" fill="var(--paper)" stroke="none"/>
  </g>
  <text class="phone-number" x="562" y="534" font-size="30" font-weight="600" fill="var(--paper)">888.417.LARK</text>
</svg>

<svg class="postcard postcard--back" viewBox="0 0 867 586" aria-label="Postcard back">
  <defs>
    <linearGradient id="backPhotoTone" x1="0" y1="0" x2="0" y2="1">
      <stop offset="0" stop-color="#3f73b8"/>
      <stop offset="0.4" stop-color="#6b7f95"/>
      <stop offset="0.75" stop-color="#6e6f72"/>
      <stop offset="1" stop-color="#4f4f4f"/>
    </linearGradient>
  </defs>
  <rect class="card-ground" width="867" height="586" fill="var(--charcoal)"/>
  <polygon class="photo" points="0,0 800,0 250,292 0,210" fill="url(#backPhotoTone)" role="img" aria-label="Photo of roofers on a white house roof among bare trees under blue sky"/>
  <polygon class="amber-stripe" points="0,210 250,292 800,0 820,0 252,306 0,224" fill="var(--amber)"/>

  <rect class="address-panel" x="457" y="31" width="379" height="524" fill="var(--paper)"/>
  <rect class="stamp-box" x="727" y="113" width="96" height="102" fill="none" stroke="var(--ink)" stroke-width="1.2"/>
  <g class="address-lines" stroke="var(--rule)" stroke-width="1.2">
    <line x1="471" y1="294" x2="823" y2="294"/>
    <line x1="471" y1="335" x2="823" y2="335"/>
    <line x1="471" y1="376" x2="823" y2="376"/>
    <line x1="471" y1="417" x2="823" y2="417"/>
    <line x1="471" y1="458" x2="823" y2="458"/>
  </g>

  <g class="offer-badge" transform="translate(203 262)">
    <polygon points="0,-80 71,-40 71,40 0,80 -71,40 -71,-40" fill="var(--badge)" stroke="var(--amber)" stroke-width="4"/>
    <polyline points="-45,-17 0,-43 45,-17" fill="none" stroke="var(--ink)" stroke-width="10"/>
    <text class="badge-text" x="0" y="-7" text-anchor="middle" font-size="17" font-weight="700" fill="var(--ink)">Get</text>
    <text class="badge-text" x="0" y="19" text-anchor="middle" font-size="26" font-weight="700" fill="var(--offer-red)">$200 off</text>
    <text class="badge-text" x="0" y="37" text-anchor="middle" font-size="17" font-weight="500" fill="var(--ink)">any repair</text>
    <text class="badge-text" x="0" y="51" text-anchor="middle" font-size="10" font-style="italic" fill="var(--ink)">*some rules</text>
    <text class="badge-text" x="0" y="60" text-anchor="middle" font-size="10" font-style="italic" fill="var(--ink)">may apply</text>
  </g>

  <text class="subhead" x="31" y="376" font-size="22" font-weight="600" fill="var(--honey)" letter-spacing="-0.3">Ensure Your Roof’s Safe Today</text>
  <text class="body-copy" font-size="17" fill="var(--paper)">
    <tspan x="31" y="410">Even if your home wasn’t directly hit by</tspan>
    <tspan x="31" y="431">the storm, high wind gusts can cause</tspan>
    <tspan x="31" y="452">unseen damage.</tspan>
  </text>

  <path class="phone-icon" d="M72 496 l7 -2 l5 9 l-4 3 q3 8 11 12 l3 -4 l9 4 l-1 7 q-20 2 -30 -29 z" fill="var(--honey)"/>
  <text class="phone-number" x="110" y="526" font-size="31" font-weight="600" fill="var(--paper)">888.417.LARK</text>
</svg>

</body>
</html>
```